Webdesign für die Veranstaltungsreihe Wolkenreigen
Zielgruppe
Für die Veranstaltungsreihe 'Wolkenreigen' soll ein Website-Design entwickelt werden, welches potentielle Besucher über die Veranstaltung informiert (Standorte, Anfahrt, Preise etc.) und gleichzeitig eine Foto- bzw. Videodokumentation der vergangenen 'Wolkenreigen' bietet.
Zielgruppe:
Personen jeder Altersgruppe, Gruppen wie (Familien, Vereine etc.)
Aufgabenstellung
Das Design sollte...
einfach und modern
nicht zu verspielt
freundlich
kreativ
innovativ
den Inhalt der Veranstaltungsreihe
...wiederspiegeln.
Bitte orientieren Sie sich an dem bestehenden Design der Eventreihe.

```html
<!DOCTYPE html>
<html lang="de">
<head>
<meta charset="utf-8">
<title>Wolkenreigen</title>
<link href="https://fonts.googleapis.com/css2?family=Exo+2:ital,wght@1,500&family=PT+Sans:wght@400;700&family=Kaushan+Script&display=swap" rel="stylesheet">
<style>
:root{
  --orange:#f39c12;
  --black:#000;
  --ink:#222;
  --body:#555;
  --rule:#ddd;
  --grey:#f2f2f2;
}
*{margin:0;padding:0;box-sizing:border-box}
html,body{width:1200px;height:2409px;overflow:hidden;background:#fff}
body{position:relative;font-family:"PT Sans",sans-serif;color:var(--body)}
.abs{position:absolute}
.script{font-family:"Kaushan Script",cursive;color:var(--ink);font-weight:400}

.header{left:0;top:0;width:1200px;height:108px;background:var(--black)}
.brand{left:90px;top:38px;font:700 30px/1 "PT Sans",sans-serif;color:var(--orange)}
.nav{right:40px;top:48px;display:flex;gap:26px;font:500 18px/1 "Exo 2",sans-serif;font-style:italic;color:#fff;text-transform:uppercase}
.nav .active{color:var(--orange)}

.hero{left:0;top:108px;width:1200px;height:527px;background:linear-gradient(100deg,#d8c4a8 0%,#8a7056 35%,#c7b197 55%,#5a4535 80%,#2a2018 100%)}
.hero-box{left:88px;top:228px;width:472px;height:205px;background:rgba(255,255,255,.72);padding:18px 15px}
.hero-box h1{font-size:32px;line-height:1.1;margin-bottom:18px}
.hero-box p{font-size:14px;line-height:24px;color:#222}
.btn{display:inline-block;background:var(--orange);color:#fff;font-size:16px;padding:10px 15px;margin-top:16px}

.dropdown{left:595px;top:110px;width:190px}
.dropdown .arrow{left:19px;top:-18px;width:0;height:0;border:9px solid transparent;border-bottom-color:var(--orange)}
.dropdown li{list-style:none;height:38px;background:var(--orange);color:#fff;font:500 15px/38px "Exo 2",sans-serif;font-style:italic;text-transform:uppercase;padding-left:16px;border-bottom:1px solid rgba(255,255,255,.3)}
.dropdown li.first{height:50px;line-height:62px}
.dropdown li.current{background:#000;margin:0 -4px;padding-left:20px}

.intro{left:88px;top:571px;width:1024px;height:190px;background:#fff}
.avatar{left:118px;top:609px;width:110px;height:142px;border-radius:50%;background:radial-gradient(circle at 45% 40%,#e8a07a,#c0392b 60%,#3a1a14)}
.intro-title{left:255px;top:608px;font-size:26px}
.intro-text{left:254px;top:663px;width:460px;font-size:13.5px;line-height:24px}
.icons{left:849px;top:643px;display:flex;gap:14px}
.icons svg{width:48px;height:48px}

.section-title{left:96px;width:1008px;display:flex;align-items:center;gap:14px}
.section-title::before,.section-title::after{content:"";flex:1;height:2px;background:var(--rule)}
.section-title h2{font-size:34px;line-height:1.1}
.dark .section-title::before,.dark .section-title::after{background:#fff}
.dark h2,.dark h3{color:#fff}

.about-card{top:831px;width:316px}
.about-card .pic{height:196px;box-shadow:0 12px 14px -8px rgba(0,0,0,.45)}
.about-card h3{font-family:"Kaushan Script",cursive;font-weight:400;font-size:17px;color:var(--ink);margin:36px 0 14px 2px}
.about-card p{font-size:13.5px;line-height:24px;text-align:justify;padding:0 2px}
.about-card .more{font-family:"Kaushan Script",cursive;font-size:13px;color:var(--ink);margin:22px 0 0 2px}

.dark{left:0;top:1285px;width:1200px;height:377px;background:linear-gradient(180deg,#2b2a22,#3a3528 50%,#1e1c17)}
.event{top:110px;width:320px;text-align:center}
.event svg{width:58px;height:58px}
.event h3{font-family:"Kaushan Script",cursive;font-weight:400;font-size:17px;margin:24px 0 14px}
.event p{color:#fff;font-size:13.5px;line-height:24px}
.view-all{left:537px;top:329px;width:89px;text-align:center;font-family:"Kaushan Script",cursive;font-size:17px;color:#fff;border-top:2px solid #fff;border-bottom:2px solid #fff;line-height:28px}

.news{top:1784px;width:237px;height:392px;border:1px solid #eee}
.news .pic{height:214px}
.news .date{left:0;top:214px;width:56px;height:177px;background:var(--grey);text-align:center;font-size:20px;line-height:24px;color:#444;padding-top:12px}
.news .date svg{display:block;margin:12px auto 0;width:26px;height:26px}
.news .body{left:65px;top:232px;width:162px}
.news h4{font-weight:400;font-size:14px;color:var(--ink);margin-bottom:8px}
.news p{font-size:11px;line-height:18px;text-align:justify}

.cta{left:0;top:2224px;width:1200px;height:119px;background:var(--black)}
.cta-text{left:105px;top:2262px;font-family:"Kaushan Script",cursive;font-size:32px;color:var(--orange)}
.ticket-badge{left:935px;top:2261px;width:153px;height:121px;background:#000;border:3px solid var(--orange);border-radius:14px;text-align:center;font:700 30px/33px "PT Sans",sans-serif;font-style:italic;color:var(--orange);padding-top:10px}
.copyright{left:95px;top:2367px;font-size:11px;color:#333}
.social{left:653px;top:2365px;display:flex;gap:8px;font-size:11px}
.social span{height:20px;line-height:20px;padding:0 6px;border-radius:3px}
.s-like{background:#4a66a0;color:#fff;font-weight:700}
.s-plus{border:1px solid #ccc;color:#c23321;font-weight:700}
.s-count{border:1px solid #ccc;color:#555}
.s-share{background:#2ba1e8;color:#fff}
</style>
</head>
<body>

<header class="header abs">
  <div class="brand abs">Wolkenreigen</div>
  <nav class="nav abs">
    <span>Startseite</span><span class="active">Standort 1</span><span>Standort 2</span><span>FAQ</span><span>AGB</span><span>Kontakt</span><span>Impressum</span>
  </nav>
</header>

<section class="hero abs" role="img" aria-label="Foto: Gäste stoßen mit Weingläsern an einer festlichen Tafel an"></section>

<div class="hero-box abs">
  <h1 class="script">Wolkenreigen Karlsruhe</h1>
  <p>Leider kein Termin in 2016! Nähere Informationen finden Sie beim Klick auf "Mehr Informationen".</p>
  <span class="btn">Mehr Informationen</span>
</div>

<ul class="dropdown abs">
  <span class="arrow abs"></span>
  <li class="first">Die Veranstaltung</li>
  <li class="current">Programm</li>
  <li>Wann &amp; Wo</li>
  <li>Tickets</li>
  <li>Fotos &amp; Videos</li>
</ul>

<div class="intro abs"></div>
<div class="avatar abs" role="img" aria-label="Rundes Foto: lachende Besucherin bei der Veranstaltung"></div>
<h2 class="script intro-title abs">Lorem Ipsum: Nutzung</h2>
<p class="intro-text abs">Lorem ipsum ist ein pseudo-lateinischer Text, der in Webdesign, Typografie, Layout und Druck anstelle von Englisch verwendet wird, um Design-Elemente über Inhalt zu betonen.</p>
<div class="icons abs">
  <svg viewBox="0 0 48 48"><circle cx="24" cy="24" r="23" fill="none" stroke="#ddd" stroke-width="1.5"/><rect x="14" y="17" width="20" height="14" rx="4" fill="#ccc"/><path d="M22 20l6 4-6 4z" fill="#fff"/></svg>
  <svg viewBox="0 0 48 48"><circle cx="24" cy="24" r="23" fill="none" stroke="#ddd" stroke-width="1.5"/><path d="M15 29v-4a9 9 0 0118 0v4" fill="none" stroke="#ccc" stroke-width="2"/><rect x="14" y="26" width="5" height="7" rx="1" fill="#ccc"/><rect x="29" y="26" width="5" height="7" rx="1" fill="#ccc"/></svg>
  <svg viewBox="0 0 48 48"><circle cx="24" cy="24" r="23" fill="none" stroke="#ddd" stroke-width="1.5"/><path d="M17 13h10l5 5v17H17z" fill="none" stroke="#ccc" stroke-width="2"/><path d="M20 30c3-6 5-10 4-11s-2 4 4 8" fill="none" stroke="#ccc" stroke-width="1.5"/></svg>
  <svg viewBox="0 0 48 48"><circle cx="24" cy="24" r="23" fill="none" stroke="#ddd" stroke-width="1.5"/><path d="M21 27l6-6M19 25l-3 3a3 3 0 004 4l3-3M29 23l3-3a3 3 0 00-4-4l-3 3" fill="none" stroke="#ccc" stroke-width="2"/></svg>
</div>

<div class="section-title abs" style="top:768px"><h2 class="script">Wer wir sind</h2></div>

<article class="about-card abs" style="left:99px">
  <div class="pic" role="img" aria-label="Foto: Brautpaar mit Blumenstrauß in einem Festsaal" style="background:linear-gradient(160deg,#c9a070,#8a5a40 50%,#3a2a24)"></div>
  <h3>Gewalt ist in der Regel</h3>
  <p>Lorem ipsum dolor sit amet, dass, wenn diese die Ursache für eine geringe Größe waren. Gewalt ist in der Regel an ihn geschrieben, gibt es keine neue Geburt. Oft assueverit es tun, ist niemand Eisen, normal oder mit Gewalt umgeworfen.</p>
  <div class="more">Read More...</div>
</article>
<article class="about-card abs" style="left:442px">
  <div class="pic" role="img" aria-label="Foto: unscharfe Lichter einer Abendfeier" style="background:linear-gradient(160deg,#2a2848,#7a4a7a 50%,#c48a80)"></div>
  <h3>Gewalt ist in der Regel</h3>
  <p>Lorem ipsum dolor sit amet, dass, wenn diese die Ursache für eine geringe Größe waren. Gewalt ist in der Regel an ihn geschrieben, gibt es keine neue Geburt. Oft assueverit es tun, ist niemand Eisen, normal oder mit Gewalt umgeworfen.</p>
  <div class="more">Read More...</div>
</article>
<article class="about-card abs" style="left:785px">
  <div class="pic" role="img" aria-label="Foto: gedeckte Festtafeln mit weißer Baumdekoration" style="background:linear-gradient(160deg,#d8dde2,#5a6068 50%,#1e2226)"></div>
  <h3>Gewalt ist in der Regel</h3>
  <p>Lorem ipsum dolor sit amet, dass, wenn diese die Ursache für eine geringe Größe waren. Gewalt ist in der Regel an ihn geschrieben, gibt es keine neue Geburt. Oft assueverit es tun, ist niemand Eisen, normal oder mit Gewalt umgeworfen.</p>
  <div class="more">Read More...</div>
</article>

<section class="dark abs" role="img" aria-label="Hintergrundfoto: abendliche Gartenfeier unter Bäumen">
  <div class="section-title abs" style="top:34px"><h2 class="script">Kommende Veranstaltung</h2></div>
  <div class="event abs" style="left:93px">
    <svg viewBox="0 0 58 58"><rect x="4" y="8" width="50" height="46" rx="3" fill="none" stroke="#f39c12" stroke-width="4"/><rect x="4" y="8" width="50" height="10" fill="#f39c12"/><rect x="14" y="2" width="4" height="12" fill="#f39c12"/><rect x="40" y="2" width="4" height="12" fill="#f39c12"/><text x="29" y="48" text-anchor="middle" font-family="PT Sans,sans-serif" font-weight="700" font-size="26" fill="#f39c12">7</text></svg>
    <h3>Gewalt ist in der Regel</h3>
    <p>Lorem ipsum dolor sit amet, dass, wenn diese die Ursache für eine geringe Größe waren. Gewalt ist in der Regel an ihn geschrieben.</p>
  </div>
  <div class="event abs" style="left:427px">
    <svg viewBox="0 0 58 58"><rect x="4" y="8" width="50" height="46" rx="3" fill="none" stroke="#f39c12" stroke-width="4"/><rect x="4" y="8" width="50" height="10" fill="#f39c12"/><rect x="14" y="2" width="4" height="12" fill="#f39c12"/><rect x="40" y="2" width="4" height="12" fill="#f39c12"/><text x="29" y="48" text-anchor="middle" font-family="PT Sans,sans-serif" font-weight="700" font-size="26" fill="#f39c12">12</text></svg>
    <h3>Gewalt ist in der Regel</h3>
    <p>Lorem ipsum dolor sit amet, dass, wenn diese die Ursache für eine geringe Größe waren. Gewalt ist in der Regel an ihn geschrieben.</p>
  </div>
  <div class="event abs" style="left:778px">
    <svg viewBox="0 0 58 58"><rect x="4" y="8" width="50" height="46" rx="3" fill="none" stroke="#f39c12" stroke-width="4"/><rect x="4" y="8" width="50" height="10" fill="#f39c12"/><rect x="14" y="2" width="4" height="12" fill="#f39c12"/><rect x="40" y="2" width="4" height="12" fill="#f39c12"/><text x="29" y="48" text-anchor="middle" font-family="PT Sans,sans-serif" font-weight="700" font-size="26" fill="#f39c12">21</text></svg>
    <h3>Gewalt ist in der Regel</h3>
    <p>Lorem ipsum dolor sit amet, dass, wenn diese die Ursache für eine geringe Größe waren. Gewalt ist in der Regel an ihn geschrieben.</p>
  </div>
  <div class="view-all abs">View All</div>
</section>

<div class="section-title abs" style="top:1711px"><h2 class="script">Was gibt's Neues?</h2></div>

<article class="news abs" style="left:96px">
  <div class="pic" role="img" aria-label="Foto: Lichterketten in Bäumen über einer Gartenfeier" style="background:linear-gradient(160deg,#2a2418,#8a6a3a 50%,#3a3020)"></div>
  <div class="date abs">06<br>Nov<svg viewBox="0 0 26 26"><path d="M3 4h20v13H10l-5 5v-5H3z" fill="none" stroke="#ccc" stroke-width="1.5"/></svg><svg viewBox="0 0 26 26"><path d="M13 22L4 13a5 5 0 019-6 5 5 0 019 6z" fill="none" stroke="#ccc" stroke-width="1.5"/></svg></div>
  <div class="body abs"><h4>Lorem Ipsum Nutzung</h4><p>Lorem ipsum ist ein pseudo-lateinischer Text, der in Webdesign, Typografie, Layout und Druck anstelle von Englisch verwendet wird, Layout und Druck anstelle von Englisch verwendet wird</p></div>
</article>
<article class="news abs" style="left:353px">
  <div class="pic" role="img" aria-label="Foto: Brautpaar unter einem Baum im Garten" style="background:linear-gradient(160deg,#b8a888,#6a6a48 50%,#2a3020)"></div>
  <div class="date abs">06<br>Nov<svg viewBox="0 0 26 26"><path d="M3 4h20v13H10l-5 5v-5H3z" fill="none" stroke="#ccc" stroke-width="1.5"/></svg><svg viewBox="0 0 26 26"><path d="M13 22L4 13a5 5 0 019-6 5 5 0 019 6z" fill="none" stroke="#ccc" stroke-width="1.5"/></svg></div>
  <div class="body abs"><h4>Lorem Ipsum Nutzung</h4><p>Lorem ipsum ist ein pseudo-lateinischer Text, der in Webdesign, Typografie, Layout und Druck anstelle von Englisch verwendet wird, Layout und Druck anstelle von Englisch verwendet wird</p></div>
</article>
<article class="news abs" style="left:610px">
  <div class="pic" role="img" aria-label="Foto: Terrasse mit Kamin und Lounge-Sesseln am Abend" style="background:linear-gradient(160deg,#3a3228,#8a7058 50%,#4a4038)"></div>
  <div class="date abs">06<br>Nov<svg viewBox="0 0 26 26"><path d="M3 4h20v13H10l-5 5v-5H3z" fill="none" stroke="#ccc" stroke-width="1.5"/></svg><svg viewBox="0 0 26 26"><path d="M13 22L4 13a5 5 0 019-6 5 5 0 019 6z" fill="none" stroke="#ccc" stroke-width="1.5"/></svg></div>
  <div class="body abs"><h4>Lorem Ipsum Nutzung</h4><p>Lorem ipsum ist ein pseudo-lateinischer Text, der in Webdesign, Typografie, Layout und Druck anstelle von Englisch verwendet wird, Layout und Druck anstelle von Englisch verwendet wird</p></div>
</article>
<article class="news abs" style="left:867px">
  <div class="pic" role="img" aria-label="Foto: beleuchtete Palmen bei einer nächtlichen Feier" style="background:linear-gradient(160deg,#1a1408,#a07828 50%,#2a2010)"></div>
  <div class="date abs">06<br>Nov<svg viewBox="0 0 26 26"><path d="M3 4h20v13H10l-5 5v-5H3z" fill="none" stroke="#ccc" stroke-width="1.5"/></svg><svg viewBox="0 0 26 26"><path d="M13 22L4 13a5 5 0 019-6 5 5 0 019 6z" fill="none" stroke="#ccc" stroke-width="1.5"/></svg></div>
  <div class="body abs"><h4>Lorem Ipsum Nutzung</h4><p>Lorem ipsum ist ein pseudo-lateinischer Text, der in Webdesign, Typografie, Layout und Druck anstelle von Englisch verwendet wird, Layout und Druck anstelle von Englisch verwendet wird</p></div>
</article>

<section class="cta abs"></section>
<div class="cta-text abs">Jetzt Karten für den Wolkenreigen kaufen!</div>
<div class="ticket-badge abs">Jetzt<br>Tickets<br>sichern!</div>

<footer>
  <div class="copyright abs">© Wolkenreigen 2016 | Impressum</div>
  <div class="social abs">
    <span class="s-like">Gefällt mir 4.887</span>
    <span class="s-plus">+1</span>
    <span class="s-count">11</span>
    <span class="s-share">Teilen</span>
  </div>
</footer>

</body>
</html>
```